Web template for real estate developing company
KORVALD
Real Estate
www.morvinkorvald.dk
Developing real estate company in Denmark.
Consulting Competence
Handling of a project:
Analysis of local conditions and market analysis
Functional and usability concept
Analysis of profitability
Financing and utilization strategies
Economic and Technical project control
Like: Start up movement on the KORVALD logo like a dynamic building assamply on a black/grey background.
Dont like: To much information and pictures on the first front page.
Elegant
black background
grey backgrund
red logo
top
http://www.lindquistaro.com/
We want to have total remake on our website www.morvinkorvald.dk .
the design and setup on this brochure can be an inspiration
logo
Please place the above jpg-photos in decending order.

```html
<!DOCTYPE html>
<html lang="da">
<head>
<meta charset="utf-8">
<title>Korvald Real Estate</title>
<link href="https://fonts.googleapis.com/css2?family=Arimo:wght@400;700&family=Open+Sans:wght@300;400;700&display=swap" rel="stylesheet">
<style>
:root{
  --bg-dark:#161616;
  --bg-content:#3a3a3a;
  --bg-footer:#2a2a2a;
  --red:#d4141c;
  --text:#c9c9c9;
  --text-dim:#9a9a9a;
  --white:#ffffff;
  --tab:#4a4a4a;
  --tab-edge:#6a6a6a;
}
*{margin:0;padding:0;box-sizing:border-box}
html,body{width:1200px;height:862px;overflow:hidden}
body{position:relative;background:var(--bg-dark);font-family:"Arimo",Arial,sans-serif;color:var(--text)}
.header{position:absolute;left:0;top:0;width:1200px;height:400px;background:linear-gradient(#1b1b1b,#111 70%,#2a2a2a)}
.brand{position:absolute;left:112px;top:30px;display:flex;align-items:center;gap:12px;font-family:"Arimo",sans-serif;font-weight:400;font-size:30px;color:#e6e6e6}
.brand i{display:block;width:16px;height:16px;background:var(--red)}
.nav{position:absolute;left:499px;top:53px;width:526px;height:38px;display:flex;background:var(--tab);border:1px solid var(--tab-edge);border-radius:4px 4px 0 0}
.nav a{flex:auto;text-align:center;line-height:36px;font-size:14px;color:#e6e6e6;text-decoration:none;border-right:1px solid #333}
.nav a:last-child{border-right:0}
.hero{position:absolute;left:168px;top:96px;width:859px;height:293px;background:#2b2b2b;border:4px solid #444;box-shadow:0 4px 14px #000}
.hero-photo{position:absolute;left:8px;top:8px;width:555px;height:269px;background:linear-gradient(135deg,#d8d8d6,#9d9d9a 45%,#6f706e)}
.contact{position:absolute;left:563px;top:8px;width:280px;height:269px;background:#111;padding:20px 18px;font-family:"Open Sans",sans-serif;color:#ddd}
.contact .addr{font-size:19px;font-weight:300;line-height:26px}
.contact .phone{margin-top:10px;font-size:22px;font-weight:700;color:var(--red)}
.contact .mail{position:absolute;left:18px;top:205px;font-size:13px;line-height:22px}
.portrait{position:absolute;right:14px;top:174px;width:66px;height:74px;background:linear-gradient(#b08a6a,#6a4a38)}
.content{position:absolute;left:0;top:400px;width:1200px;height:280px;background:var(--bg-content)}
.intro{position:absolute;left:175px;top:18px;width:500px}
.intro h1{font-family:"Open Sans",sans-serif;font-weight:400;font-size:19px;color:var(--red);margin-bottom:16px}
.intro p{font-size:11.5px;line-height:16px;color:var(--text);margin-bottom:10px}
.intro p.motto{font-weight:700;color:#eee}
.btn{display:inline-flex;align-items:center;gap:8px;margin-top:4px;padding:4px 16px 4px 8px;background:#1f1f1f;border-radius:12px;font-size:12px;color:#eee}
.btn svg{display:block}
.services{position:absolute;left:768px;top:18px;width:260px}
.services h2{font-family:"Open Sans",sans-serif;font-weight:400;font-size:19px;color:#e4e4e4;margin-bottom:12px}
.services li{list-style:none;font-size:11.5px;line-height:27.6px;color:var(--text);padding-left:14px;position:relative}
.services li::before{content:"";position:absolute;left:0;top:11px;width:5px;height:5px;background:var(--text-dim)}
.partners{position:absolute;left:168px;top:686px;width:859px;height:82px;background:var(--white);border:3px solid #555;display:flex;align-items:center;justify-content:space-around;padding:0 34px}
.partner{display:flex;align-items:center;gap:6px;font-family:"Arimo",sans-serif;font-weight:700;font-size:15px;color:#333}
.partner i{display:block;width:14px;height:14px;background:#c4161c}
.arrow{position:absolute;top:22px}
.arrow.left{left:4px}
.arrow.right{right:4px}
.footer{position:absolute;left:0;top:780px;width:1200px;height:82px;background:var(--bg-footer)}
.footer-nav{position:absolute;left:170px;top:16px;font-size:12px;color:#bbb}
.footer-nav span{margin:0 10px}
.footer-nav span:first-child{margin-left:0}
.copyright{position:absolute;left:170px;top:42px;font-size:11px;color:#8a8a8a}
.footer-brand{position:absolute;left:920px;top:26px;font-family:"Arimo",sans-serif;font-weight:400;font-size:20px;color:#cfcfcf}
</style>
</head>
<body>
<header class="header">
  <div class="brand"><i></i>Korvald</div>
  <nav class="nav">
    <a href="#">Forside</a><a href="#">Byggen</a><a href="#">Projektudvikling</a><a href="#">Referencer</a><a href="#">Kontakt</a>
  </nav>
  <section class="hero">
    <div class="hero-photo" role="img" aria-label="Concrete wall elements being assembled on a construction site with a worker in a high-visibility vest"></div>
    <div class="contact">
      <div class="addr">Halvmosevej 22<br>7100 Vejle, Danmark</div>
      <div class="phone">Tlf.: 75 12 34 56</div>
      <div class="portrait" role="img" aria-label="Portrait of the contact person"></div>
      <div class="mail">Mail: post@morvinkorvald.dk<br>www.morvinkorvald.dk</div>
    </div>
  </section>
</header>

<main class="content">
  <div class="intro">
    <h1>Kvalitetsbyggeri til erhvervslivet</h1>
    <p>Med blik for det funktionelle og arkitektoniske opføres Korvald kvalitetsbyggeri over hele landet. Vi lytter til vores kunders ønsker og tilpasser byggeriet efter deres behov.</p>
    <p>Vi har stor erfaring i at opføre alle former for erhvervsbyggeri. Med en stærk økonomi er vi i stand til at løfte store opgaver.</p>
    <p>Vi samarbejder kun med underentreprenører, som lever op til vores høje kvalitetskrav, og vi vægter et tillidsfuldt samarbejde højt.</p>
    <p class="motto">Vi holder altid det vi lover, og gør det vi siger.</p>
    <span class="btn"><svg width="14" height="14" viewBox="0 0 14 14"><circle cx="7" cy="7" r="7" fill="#888"/><path d="M5 4l4 3-4 3z" fill="#1f1f1f"/></svg>Se vores brochure</span>
  </div>
  <aside class="services">
    <h2>Services</h2>
    <ul>
      <li>Consulting Competence</li>
      <li>Handling project</li>
      <li>Analysis of local conditions and market analysis</li>
      <li>Functional and usability concept</li>
      <li>Financing and utilization strategies</li>
      <li>Economic and Technical project control</li>
    </ul>
  </aside>
</main>

<section class="partners">
  <svg class="arrow left" width="18" height="30" viewBox="0 0 18 30"><path d="M14 3L4 15l10 12" fill="none" stroke="#333" stroke-width="4"/></svg>
  <div class="partner"><i></i>Sydvent Tagværk</div>
  <div class="partner">Brinso Trapper</div>
  <div class="partner">K.B. Vendrup &amp; Søn</div>
  <div class="partner">FA. Nels Gorlund</div>
  <div class="partner">Trovik VVS &amp; Energi</div>
  <svg class="arrow right" width="18" height="30" viewBox="0 0 18 30"><path d="M4 3l10 12L4 27" fill="none" stroke="#333" stroke-width="4"/></svg>
</section>

<footer class="footer">
  <div class="footer-nav"><span>Forside</span>|<span>Byggen</span>|<span>Projektudvikling</span>|<span>Referencer</span>|<span>Kontakt</span></div>
  <div class="copyright">© 2013 korvaldrealestate.com, All Right Reserved</div>
  <div class="footer-brand">Korvald</div>
</footer>
</body>
</html>
```